New Website for QWRB Holdings (Property Leasing Company in New Haven)

Design a fully functioning website for a real estate property leasing company. The company has a few properties in New Haven, CT and would like to provide an option for its tenants to pay their rent online. The company should have the ability to generate unique account log in username and password for its tenants so they can make online payments through ACH the website. (The ACH processing part will be coordinated with the bank).

Please take a look at all the pictures I uploaded of New Haven especially the area around Marlow College, you will find that the general style is Gothic and charming.

Also please make use of the pictures of the two properties I have attached to the description.

Please keep Holdings page, Contact Us Page , About Us Page, and please add a page entitled "Tenants".

On the Holdings page I would like to see on the left hand side an interactive map of new haven (Please see a map attached), split by New Haven's neighbourhoods, and showing my properties as pins of sort on the map (I can send you the addresses of the properties upon request). On the same page on the right side I want to see a drop down menu that includes list of New Haven Neighbourhoods. When a neighbourhood is selected you can see in the space underneath the drop-down menu the properties we have in that neighbourhood in large thumbnail format. Also on the map you can see the pins corresponding to those properties change colour. A user can either click on the pin or on the thumbnails to have view more pictures of the property and some details in text.

The tenants page should prompt a login to access- I like your idea of having the company name in two colours, one for QWRB and another for Holdings.Please let me know if you have any questions along the way

-------------------------------------------------------------------------------
Property Descriptions for Holdings Page
The Larch Lodge,

Neighbourhood: Westville
Name: Silas Brennaway House
Building Style: Queen Anne Style
Address: 418 Pellwin Road, New Haven, CT 06515
Number of Units: 3
Unit Names: Unit 1, Unit 2, Unit 3

Property Description

This Westiville home was built in 1897, historically known as The Silas Brennaway House, it is an example of the Queen Anne style. The large carriage house is still intact and sits in the lovely, expansive back garden! An outstanding architectural feature of the house is the turret, giving the home prominence on Pellwin Road. This well maintained home has renovated kitchens in all units, the first floor has granite and red oak cabinetry. New baths and central air in all apartments. All newer mechanicals for each unit, all natural gas. The entire house has replacement windows. The new back deck overlooks the back garden and carriage house. The front steps and porch have also been rebuilt. Roof has 30 year architectural singles and approximately 15 years old, the chimney has just been lined.

Unit 1 Description:

2 Bedrooms, 6 rooms in total.
Amenities: Dishwasher, Central Air, Gas Heating, Porch

Unit 2 Description:

2 Bedrooms, 5 rooms in total.
Amenities: Dishwasher, Central Air, Gas Heating, Balcony

Unit 3 Description:

2 Bedrooms, 4 rooms in total.
Amenities: Dishwasher, Central Air, Gas Heating

The Fern Lodge:

Neighbourhood: East Rock
Name: 64 Birchmere
Building Style: Victorian
Address: 64 Birchmere Lane, New Haven, CT 06511
Number of Units: 2
Unit Names: Unit 1, and Unit 2

Property Description

East Rock incredibly charming newly renovated 2 family on quiet tree-lined block. Tenants are responsible for all utilities (gas heat, electricity and cable). Small pets are possible with landlord approval. Tenants has use of shared yard, laundry in the basement and on street parking only. Located steps away from gourmet markets & minutes to Downtown New Haven, Marlow & local hospitals. Fascinating backyard. This is a feel good house!

Unit 1 Description:

Area:
1100 soft, 3 Bedrooms, 5 rooms in total.
Amenities: In unit Washer and Dryer, Central Air, Gas Heating, Porch, Backyard

Unit 2 Description:

Area: 2,820 sqft
5 Bedrooms, 8 rooms in total.
Amenities: In unit Washer and Dryer, Dishwasher, Central Air, and Gas Heating

Target Market(s)

1-3 bedroom Renting Market around Marlow College and New Haven Community

Industry/Entity Type

Real Estate

Coding

Coded - Design and coding required

Number of Pages Required

4 page

Font styles to use
Other font styles liked:
• Helvetica

Colors
85cae6
cee9f5
d9d9d9
9d9d9d

Requirements
Must have
• Payment page with login (accounts can only be created by administrator)
• A page showcasing the properties (Professional photos to be uploaded shortly)
• A page for technical support, contact information and so forth
• Home page
Nice to have
• A professional, but stylish design. Not too colourful, something with pastel colours
Should not have
• A lot of colours, any pop-ups,

```html
<!DOCTYPE html>
<html lang="en">
<head>
<meta charset="utf-8">
<title>QWRB Holdings</title>
<link href="https://fonts.googleapis.com/css2?family=Open+Sans:wght@400;600;700;800&display=swap" rel="stylesheet">
<style>
:root{
  --blue:#85cae6;
  --blue-pale:#cee9f5;
  --grey-light:#d9d9d9;
  --grey:#9d9d9d;
  --ink:#4a4a4a;
  --dark:#2c2e30;
  --white:#ffffff;
}
*{margin:0;padding:0;box-sizing:border-box}
html,body{width:711px;height:1200px;overflow:hidden;background:var(--white)}
body{position:relative;font-family:"Open Sans",Helvetica,Arial,sans-serif;color:var(--ink)}

/* hero */
.hero{position:absolute;left:0;top:0;width:711px;height:392px;background:linear-gradient(180deg,#6f8ea6 0%,#8ba78b 38%,#5d7a52 62%,#3e4e3a 100%)}
.hero-cut{position:absolute;left:0;top:0}
.topbar{position:absolute;left:0;top:0;width:711px;height:62px;background:rgba(30,34,38,.55)}
.brand{position:absolute;left:28px;top:16px;display:flex;align-items:center;gap:8px;color:var(--white);font-weight:800;font-size:17px;letter-spacing:.5px;line-height:1}
.brand-mark{width:22px;height:22px;background:var(--white)}
.social-top{position:absolute;left:414px;top:10px;display:flex;gap:6px}
.social-top span,.social-foot span{width:15px;height:15px;background:var(--white);display:block}
.phone-top{position:absolute;left:488px;top:9px;display:flex;align-items:center;gap:6px;color:var(--white);font-size:13px;font-weight:600}
.nav{position:absolute;left:392px;top:36px;display:flex;gap:4px}
.nav a{color:var(--white);text-decoration:none;font-size:10.5px;font-weight:600;padding:4px 9px}
.nav a.active{color:var(--blue);border-bottom:2px solid var(--blue)}
.tagline{position:absolute;left:0;top:330px;width:711px;height:38px;background:rgba(30,34,38,.45);color:var(--white);font-size:19px;font-weight:700;text-align:center;line-height:38px}

/* about */
.about{position:absolute;left:0;top:396px;width:711px;text-align:center}
.section-title{font-size:21px;font-weight:700;letter-spacing:.3px}
.section-title em{font-style:normal;color:var(--blue)}
.about .section-title{color:#555}
.rule{width:620px;height:1px;background:var(--grey-light);margin:10px auto 12px}
.about p{width:620px;margin:0 auto;font-size:10px;line-height:15px;color:#666;text-align:center}
.read-more{display:inline-flex;align-items:center;gap:5px;margin-top:10px;font-size:11px;font-weight:700;color:#444}
.read-more i{width:11px;height:11px;border-radius:50%;background:var(--ink);display:block;position:relative}
.read-more i::after{content:"";position:absolute;left:3px;top:3px;border-left:5px solid var(--white);border-top:2.5px solid transparent;border-bottom:2.5px solid transparent}

/* featured */
.featured{position:absolute;left:0;top:548px;width:711px;height:300px;background:linear-gradient(180deg,#3b3c3a 0%,#5a4a38 40%,#6b5a3e 70%,#3a3834 100%)}
.featured .section-title{position:absolute;left:0;top:22px;width:711px;text-align:center;color:var(--white)}
.arrow{position:absolute;top:150px}
.cards{position:absolute;left:78px;top:70px;display:flex;gap:9px}
.card{width:135px}
.card-photo{width:135px;height:110px;border:2px solid var(--white)}
.card h3{font-size:11px;font-weight:700;color:var(--white);margin-top:6px}
.card p{font-size:7.5px;line-height:10px;color:#e6e6e6;margin-top:2px}
.pay-btn{display:inline-block;margin-top:5px;background:var(--blue-pale);color:#333;font-size:8px;font-weight:700;padding:2px 8px}
.pay-btn::after{content:" \25B8"}

/* inquiry + contact */
.contact-band{position:absolute;left:0;top:848px;width:711px;height:220px;background:linear-gradient(135deg,#f1f2ee 0%,#e7ebe1 50%,#eef0ec 100%)}
.panel{position:absolute;top:24px;background:rgba(255,255,255,.85);padding:10px 12px}
.panel h2{font-size:13.5px;font-weight:700;color:#555;padding-bottom:5px;border-bottom:1px solid var(--grey)}
.inquiry{left:30px;width:305px;height:180px}
.inquiry small{display:block;font-size:7.5px;color:#777;margin:5px 0 6px}
.field{width:205px;height:15px;border:1px solid var(--grey-light);background:var(--white);font-size:7.5px;color:#888;padding:2px 5px;margin-bottom:5px}
.submit{position:absolute;right:95px;bottom:12px;background:var(--dark);color:var(--white);font-size:9px;font-weight:700;padding:3px 10px}
.info{left:368px;width:292px;height:180px}
.info-row{display:flex;align-items:center;gap:10px;margin-top:12px;font-size:9.5px;font-weight:600;color:#444;line-height:12px}
.info-row svg{flex:none}

/* footer */
.footer{position:absolute;left:0;top:1068px;width:711px;height:132px;background:var(--dark)}
.foot-links{position:absolute;left:30px;top:20px;font-size:9.5px;color:#ddd}
.foot-links span{margin:0 6px;color:var(--grey)}
.copyright{position:absolute;left:30px;top:50px;font-size:9px;color:#bbb}
.foot-brand{position:absolute;right:30px;top:14px;font-size:19px;font-weight:700;color:var(--blue)}
.social-foot{position:absolute;right:30px;top:46px;display:flex;gap:8px}
</style>
</head>
<body>

<header class="hero" role="img" aria-label="Photo of a green Victorian house with a turret and porch among trees">
  <svg class="hero-cut" width="711" height="392" viewBox="0 0 711 392"><polygon points="0,392 711,356 711,392" fill="#ffffff"/></svg>
  <div class="topbar"></div>
  <div class="brand"><span class="brand-mark"></span>QWRB HOLDINGS</div>
  <div class="social-top"><span></span><span></span><span></span></div>
  <div class="phone-top">
    <svg width="16" height="16" viewBox="0 0 16 16"><circle cx="8" cy="8" r="7" fill="none" stroke="#fff" stroke-width="1.3"/><path d="M5.5 4.5l1.5 0 .7 2-1 .8c.5 1 1.2 1.7 2.2 2.2l.8-1 2 .7 0 1.5c-3.5.3-6.5-2.7-6.2-6.2z" fill="#fff"/></svg>
    012-555-0147
  </div>
  <nav class="nav"><a class="active">HOME</a><a>ABOUT</a><a>PROPERTIES</a><a>CONTACT US</a></nav>
  <div class="tagline">We Provide Real Estate Property Leasing Company</div>
</header>

<section class="about">
  <h2 class="section-title">ABOUT <em>QWRB HOLDINGS</em></h2>
  <div class="rule"></div>
  <p>Lorem ipsum dolor sit amet, consectetuer adipiscing elit, sed diam nonummy nibh euismod tincidunt ut laoreet dolore magna aliquam erat volutpat. Ut wisi enim ad minim veniam, quis nostrud exerci tation ullamcorper suscipit lobortis nisl ut aliquip ex ea commodo consequat. Duis autem vel eum iriure dolor in hendrerit in vulputate velit esse molestie consequat, vel illum dolore eu feugiat nulla facilisis at vero eros et accumsan et iusto odio dignissim qui blandit praesent luptatum zzril delenit augue duis dolore te feugait nulla facilisi.</p>
  <div class="read-more">Read More <i></i></div>
</section>

<section class="featured" role="img" aria-label="Aerial photo of New Haven town in autumn colours">
  <h2 class="section-title">FEATURED <em>PROPERTY</em></h2>
  <svg class="arrow" style="left:22px" width="14" height="24" viewBox="0 0 14 24"><polyline points="12,2 2,12 12,22" fill="none" stroke="#fff" stroke-width="2"/></svg>
  <svg class="arrow" style="left:675px" width="14" height="24" viewBox="0 0 14 24"><polyline points="2,2 12,12 2,22" fill="none" stroke="#fff" stroke-width="2"/></svg>
  <div class="cards">
    <article class="card">
      <div class="card-photo" role="img" aria-label="Photo of a house" style="background:linear-gradient(160deg,#9fb3c2,#6f6a5a)"></div>
      <h3>Lorem ipsum dolor</h3>
      <p>Lorem ipsum dolor sit amet lorem ipsum dolor sit amet consectetur</p>
      <span class="pay-btn">Pay Rent</span>
    </article>
    <article class="card">
      <div class="card-photo" role="img" aria-label="Photo of a college tower" style="background:linear-gradient(160deg,#a9c4d8,#8a6f55)"></div>
      <h3>Lorem ipsum dolor</h3>
      <p>Lorem ipsum dolor sit amet lorem ipsum dolor sit amet consectetur</p>
      <span class="pay-btn">Pay Rent</span>
    </article>
    <article class="card">
      <div class="card-photo" role="img" aria-label="Photo of a town green with trees" style="background:linear-gradient(160deg,#b7d0e0,#5f8a4c)"></div>
      <h3>Lorem ipsum dolor</h3>
      <p>Lorem ipsum dolor sit amet lorem ipsum dolor sit amet consectetur</p>
      <span class="pay-btn">Pay Rent</span>
    </article>
    <article class="card">
      <div class="card-photo" role="img" aria-label="Photo of city buildings" style="background:linear-gradient(160deg,#9bb8cf,#a0624a)"></div>
      <h3>Lorem ipsum dolor</h3>
      <p>Lorem ipsum dolor sit amet lorem ipsum dolor sit amet consectetur</p>
      <span class="pay-btn">Pay Rent</span>
    </article>
  </div>
</section>

<section class="contact-band" role="img" aria-label="Faint street map of New Haven in the background">
  <form class="panel inquiry">
    <h2>QUICK INQUIRY</h2>
    <small>Lorem ipsum dolor sit amet consectetuer adipiscing elit sed diam nonummy</small>
    <div class="field">Firstname</div>
    <div class="field">Lastname</div>
    <div class="field">Email</div>
    <div class="field">Phone</div>
    <span class="submit">SUBMIT</span>
  </form>
  <div class="panel info">
    <h2>CONTACT INFO</h2>
    <div class="info-row">
      <svg width="20" height="20" viewBox="0 0 20 20"><circle cx="10" cy="10" r="10" fill="#555"/><path d="M10 4a4 4 0 0 0-4 4c0 3 4 8 4 8s4-5 4-8a4 4 0 0 0-4-4z" fill="#fff"/><circle cx="10" cy="8" r="1.5" fill="#555"/></svg>
      <span>Street Name, City Name Dolor Sit Amet<br>Consectetuer Adipiscing 01234</span>
    </div>
    <div class="info-row">
      <svg width="20" height="20" viewBox="0 0 20 20"><circle cx="10" cy="10" r="10" fill="#555"/><path d="M6.5 5.5h2l1 2.5-1.3 1c.6 1.3 1.5 2.2 2.8 2.8l1-1.3 2.5 1v2c-4.5.4-8.4-3.5-8-8z" fill="#fff"/></svg>
      <span>012-555-0147</span>
    </div>
    <div class="info-row">
      <svg width="20" height="20" viewBox="0 0 20 20"><circle cx="10" cy="10" r="10" fill="#555"/><rect x="5" y="6.5" width="10" height="7" fill="#fff"/><polyline points="5,6.5 10,10.5 15,6.5" fill="none" stroke="#555" stroke-width="1"/></svg>
      <span>info@qwrb-holdings.com</span>
    </div>
  </div>
</section>

<footer class="footer">
  <div class="foot-links">Home<span>|</span>About<span>|</span>Properties<span>|</span>Contact Us</div>
  <div class="copyright">© 2015 QWRB HOLDINGS. All Rights Reserved</div>
  <div class="foot-brand">QWRB HOLDINGS</div>
  <div class="social-foot"><span></span><span></span><span></span></div>
</footer>

</body>
</html>
```